Movie poster for short film: TINDERLOCK

We need a creative, artistic, stylized poster design for our short film TINDERLOCK. We would like to see designs with graphics and bold colors more than photographs. The photographs we are posting are more for reference- you do not have to use them in the poster! We are looking for something clean and simple. The film is a drama so please don't make it funny. The mood of the film is thoughtful and introspective. Name of film should be in all caps. Things to include in the poster:
Name of film: TINDERLOCK
Lantern Hollow Productions
Starring Marisa Kovalenko

Here is a brief plot synopsis: TINDERLOCK follows one night in the life of a rebellious young woman who breaks into a diner after hours with a can of spray paint. Her intentions change after she ends up discovering what's left of a love story.

The movie is somewhat experimental, set to music for part of it with no dialog. The whole movie takes place in an old fashioned diner.

Target Market(s)

Film festival attendees between the ages of 20-50

Industry/Entity Type

Movie

Font styles to use
Sans Serif

Requirements
Must have
• See project description above- also the film is somewhat dark in nature so please don't make it too 'happy' looking.

```html
<!DOCTYPE html>
<html lang="en">
<head>
<meta charset="utf-8">
<title>TINDERLOCK — Poster</title>
<link rel="stylesheet" href="https://fonts.googleapis.com/css2?family=Bebas+Neue&display=swap">
<style>
  :root {
    --paper: #ffffff;
    --frame: #8a8a8a;
    --ink: #0a0a0a;
    --coral: #f48d71;
    --ember: #772d26;
  }
  * { margin: 0; padding: 0; box-sizing: border-box; }
  html, body {
    width: 789px;
    height: 1200px;
    overflow: hidden;
    background: var(--paper);
  }
  .poster {
    position: relative;
    width: 789px;
    height: 1200px;
    background: var(--paper);
    border: 1px solid var(--frame);
    overflow: hidden;
    font-family: "Bebas Neue", "Arial Narrow", sans-serif;
    color: var(--ink);
  }
  .splatter {
    position: absolute;
    background: var(--ink);
    border-radius: 46% 54% 50% 50% / 52% 44% 56% 48%;
  }
  .splatter--top { left: 92px; top: 140px; width: 110px; height: 110px; }
  .splatter--bottom { left: 660px; top: 585px; width: 105px; height: 110px; }
  .title-art {
    position: absolute;
    inset: 0;
    width: 789px;
    height: 1200px;
  }
  .title-art text {
    font-family: "Bebas Neue", "Arial Narrow", sans-serif;
    font-size: 212px;
  }
  .studio, .billing {
    position: absolute;
    font-size: 36px;
    line-height: 1;
    letter-spacing: 0.2px;
    text-transform: uppercase;
    white-space: nowrap;
  }
  .studio { left: 285px; top: 166px; }
  .billing { left: 351px; top: 808px; }
</style>
</head>
<body>
  <main class="poster">
    <div class="splatter splatter--top" role="img" aria-label="Black ink splatter"></div>
    <div class="splatter splatter--bottom" role="img" aria-label="Black ink splatter"></div>

    <svg class="title-art" viewBox="0 0 789 1200" aria-labelledby="film-title">
      <defs>
        <clipPath id="blob-clip">
          <path d="M375 260 C520 262 690 280 682 460 C675 600 620 728 450 724 C300 720 150 700 152 560 C154 400 230 258 375 260 Z"/>
        </clipPath>
      </defs>
      <path class="blob" fill="var(--coral)" d="M375 260 C520 262 690 280 682 460 C675 600 620 728 450 724 C300 720 150 700 152 560 C154 400 230 258 375 260 Z"/>
      <text id="film-title" x="39" y="570" fill="var(--ink)" textLength="700" lengthAdjust="spacingAndGlyphs">TINDERLOCK</text>
      <g clip-path="url(#blob-clip)" aria-hidden="true">
        <text x="39" y="570" fill="var(--ember)" textLength="700" lengthAdjust="spacingAndGlyphs">TINDERLOCK</text>
      </g>
    </svg>

    <p class="studio">Lantern Hollow Productions</p>
    <p class="billing">Starring Marisa Kovalenko</p>
  </main>
</body>
</html>
```